Advertising brochure for Wander With Kestrel

We need a new single sided DL flier for the 2020 season!<br/>This flier is for our tour business. You can find all the details about the tour at our web site http://wanderkestrel.tourvista.example<br/>The flier needs to grab the tourists attention, explain the tour and give price. I will upload a copy of last year's flier for your reference.<br/>We'd like the flier to match our web site to some extent.<br/>The most up to date information is on the web site and NOT last year's brochure. Use the web site for tour itinerary. We NO LONGER do the "Golf Course".<br/>Remember the size is "DL". Please no A4 format etc.<br/>You will be able to source images from:<br/>- Our web site<br/>- Our Chatterbook<br/>- Voyagerank<br/>- Plinko Listings<br/>If you have a particular idea in mind then feel free to contact us and we will try to accommodate your photo request.<br/>Good luck!

Target Market(s)

All ages

Industry/Entity Type

Tourism

Requirements
Must have
• Phone number
• Web Site
• Email address
• Price
Nice to have
• Description of tour and images

```html
<!DOCTYPE html>
<html lang="en">
<head>
<meta charset="utf-8">
<title>Wander With Kestrel – DL Flier</title>
<link rel="stylesheet" href="https://fonts.googleapis.com/css2?family=Roboto:wght@300;400;500;700;900&family=Oswald:wght@600&family=Source+Sans+3:wght@400;600;700&display=swap">
<style>
  :root {
    --backdrop: #202022;
    --paper: #eeede9;
    --paper-shade: #e2e0d9;
    --orange: #f5821f;
    --orange-light: #f9b871;
    --yellow: #fdb913;
    --cream: #fbeeb0;
    --brown: #9c4f16;
    --ink: #141414;
    --body: #2a2a2a;
    --white: #ffffff;
  }
  * { box-sizing: border-box; margin: 0; padding: 0; }
  html, body { width: 848px; height: 1200px; overflow: hidden; background: var(--backdrop); }
  .flier {
    position: absolute; left: 139px; top: 0; width: 570px; height: 1200px;
    background: radial-gradient(ellipse at 40% 40%, var(--paper) 0%, var(--paper-shade) 100%);
    overflow: hidden; font-family: "Source Sans 3", sans-serif; color: var(--body);
  }
  .web-tab { position: absolute; left: 0; top: 0; width: 332px; height: 48px; }
  .web-tab span {
    position: absolute; left: 30px; top: 14px; font-family: "Roboto", sans-serif;
    font-weight: 700; font-size: 16px; color: var(--ink);
  }
  .brand { position: absolute; left: 28px; top: 140px; width: 300px; }
  .brand-dot { width: 46px; height: 46px; border-radius: 50%; background: var(--orange); margin-bottom: 14px; }
  .brand-name {
    font-family: "Roboto", sans-serif; font-weight: 900; font-size: 44px;
    line-height: 1.02; color: var(--orange); text-transform: uppercase;
  }
  .intro { position: absolute; left: 352px; top: 42px; width: 168px; font-family: "Roboto", sans-serif; }
  .intro h2 { font-size: 15.5px; font-weight: 700; line-height: 1.33; color: var(--ink); }
  .intro p { margin-top: 9px; font-size: 16px; font-weight: 300; line-height: 1.28; color: var(--ink); }
  .intro em { font-style: italic; font-weight: 700; color: var(--orange); }
  .price {
    position: absolute; left: 350px; top: 256px; font-family: "Roboto", sans-serif;
    font-weight: 900; font-size: 88px; line-height: 1; color: var(--ink); letter-spacing: -1px;
  }
  .per-person {
    position: absolute; left: 352px; top: 346px; font-family: "Roboto", sans-serif;
    font-weight: 700; font-size: 25px; color: var(--ink);
  }
  .kids-strip {
    position: absolute; left: 534px; top: 45px; width: 24px; height: 330px; background: var(--yellow);
  }
  .kids-strip span {
    position: absolute; left: 50%; top: 50%; white-space: nowrap;
    transform: translate(-50%, -50%) rotate(-90deg);
    font-family: "Roboto", sans-serif; font-size: 14px; font-weight: 400; color: var(--ink);
  }
  .tour-title {
    position: absolute; left: 31px; top: 384px; font-family: "Oswald", sans-serif;
    font-weight: 600; font-size: 58px; line-height: 1.1; color: var(--brown); letter-spacing: 0.5px;
  }
  .book-bar {
    position: absolute; left: 274px; top: 398px; width: 296px; height: 36px; background: var(--orange-light);
    font-family: "Oswald", sans-serif; font-weight: 600; font-size: 24px;
    color: var(--brown); line-height: 36px; padding-left: 16px;
  }
  .divider { position: absolute; left: 259px; top: 483px; width: 1px; height: 394px; background: var(--orange-light); }
  .item { position: absolute; }
  .item h3 {
    font-family: "Roboto", sans-serif; font-weight: 500; font-size: 19.5px;
    line-height: 1.25; color: var(--ink); margin-bottom: 8px;
  }
  .item p { font-size: 13.5px; line-height: 1.45; color: var(--body); }
  .col-left { left: 31px; width: 212px; }
  .col-right { left: 282px; width: 258px; }
  .photo {
    position: absolute; left: 0; top: 915px; width: 570px; height: 285px;
    background: linear-gradient(100deg, #6e4a33 0%, #b48866 30%, #e5d8c8 55%, #8c6a4e 80%, #3d2a1e 100%);
  }
  .photo::after {
    content: ""; position: absolute; inset: 0;
    background: linear-gradient(180deg, rgba(0,0,0,0) 45%, rgba(20,10,5,0.55) 100%);
  }
  .waves { position: absolute; left: 0; top: 850px; width: 570px; height: 130px; }
  .contact { position: absolute; left: 0; top: 1124px; width: 570px; text-align: center; }
  .contact-call {
    font-family: "Source Sans 3", sans-serif; font-weight: 700; font-size: 23px;
    color: var(--yellow); text-shadow: 0 1px 3px rgba(0,0,0,0.6);
  }
  .contact-lines {
    margin-top: 2px; font-weight: 600; font-size: 19px; color: var(--white);
    text-shadow: 0 1px 3px rgba(0,0,0,0.7);
  }
</style>
</head>
<body>
<main class="flier">
  <svg class="web-tab" viewBox="0 0 332 48" aria-hidden="true">
    <path d="M0 0 H318 L332 48 H0 Z" fill="var(--yellow)"/>
  </svg>
  <div class="web-tab"><span>wanderkestrel.tourvista.example</span></div>

  <div class="brand">
    <div class="brand-dot"></div>
    <div class="brand-name">Wander<br>With<br>Kestrel</div>
  </div>

  <section class="intro">
    <h2>A UNIQUE TAG-ALONG JOURNEY THROUGH COOBER PEDY.</h2>
    <p>Enjoy a <em>tour from the comfort of your own car as our experienced guide</em> takes you through a "day in the life" of a Coober Pedy Miner.</p>
  </section>

  <div class="price">$40</div>
  <div class="per-person">Per PERSON</div>

  <div class="kids-strip"><span>(Kids half price and Children under 5 free!)</span></div>

  <h1 class="tour-title">THE TOUR</h1>
  <div class="book-bar">(08) 5550 1427 to book</div>

  <div class="divider"></div>

  <article class="item col-left" style="top:484px">
    <h3>Underground Home</h3>
    <p>Our guide's family open the doors of their home and give you a guided tour of their dugout.</p>
  </article>
  <article class="item col-left" style="top:596px">
    <h3>Noodling</h3>
    <p>Next we hit the noodling field to try and find our own opal. With our expert guide showing you how to find opal you'll be a pro in no time!</p>
  </article>
  <article class="item col-left" style="top:727px">
    <h3>Opal Cutting and<br>Polishing</h3>
    <p>We'll finish up our tour with an opal cutting and polishing demonstration and who knows?... It might be your opal we cut and polish!</p>
  </article>

  <article class="item col-right" style="top:481px">
    <h3>Safety Gear</h3>
    <p>All safety gear will be provided for you including helmets and UHF radios. Your safety is our number one priority!</p>
  </article>
  <article class="item col-right" style="top:596px">
    <h3>Opal Mining</h3>
    <p>We'll make our way down an underground mine where we'll show you the different techniques that modern miners use to extract this beautiful stone.</p>
  </article>
  <article class="item col-right" style="top:727px">
    <h3>Drive through the field</h3>
    <p>Making our way into town, via the opal fields, you'll get a front row seat for viewing our magical landscape that has been terraformed with over 100 years of mining.</p>
  </article>

  <div class="photo" role="img" aria-label="Photo of an underground dugout bedroom with rough sandstone walls, bunk beds and a colourful rug"></div>

  <svg class="waves" viewBox="0 0 570 130" preserveAspectRatio="none" aria-hidden="true">
    <path d="M0 58 C150 50 300 60 420 45 C490 36 540 20 570 2 V40 C520 70 430 96 300 96 C180 96 100 72 0 68 Z" fill="var(--cream)"/>
    <path d="M0 66 C100 70 180 94 300 94 C430 94 520 68 570 38 V60 C520 88 430 108 300 106 C180 104 100 82 0 76 Z" fill="var(--orange)"/>
    <path d="M0 76 C100 82 180 104 300 106 C430 108 520 88 570 60 V95 C520 108 440 118 320 116 C200 114 100 90 0 82 Z" fill="var(--yellow)"/>
  </svg>

  <footer class="contact">
    <p class="contact-call">Contact us for further information or to book!</p>
    <p class="contact-lines">hello@wanderkestrel.example, (08) 5550 1427 to book</p>
  </footer>
</main>
</body>
</html>
```